Leading Technology Rental Company Need a graphic design to put on homepage

We need a graphic design for a new webpage for our company - Kelvo Rentals. We specialize in the technology rental for Convention/Trade shows/Compnay Events/Training/Weddings/.... Looking to create a new graphic design for a landing page which will project the right image and message.

new webpage in progress http://www.kelvorentalsbay.com/home

Looking to replace the rotating equipment images with a single image that will project best-in-class equipment/services/reliable. image also need to include a bold message statement.

```html
<!DOCTYPE html>
<html lang="en">
<head>
<meta charset="utf-8">
<title>Kelvo Rentals – Knowledge. Experience. Results.</title>
<link href="https://fonts.googleapis.com/css2?family=Roboto:wght@300;700&display=swap" rel="stylesheet">
<style>
  :root {
    --page-bg: #ececec;
    --teal-dark: #053f3c;
    --teal-mid: #0b5a55;
    --teal-light: #15706a;
    --text-white: #ffffff;
    --product-light: #e9eaea;
    --product-mid: #b9bcbc;
    --product-dark: #2a2c2d;
  }
  html, body {
    margin: 0;
    padding: 0;
    width: 1200px;
    height: 637px;
    overflow: hidden;
    background: var(--page-bg);
  }
  .hero-banner {
    position: absolute;
    left: 30px;
    top: 93px;
    width: 1140px;
    height: 451px;
    overflow: hidden;
    font-family: "Roboto", Arial, sans-serif;
    color: var(--text-white);
  }
  .hero-backdrop {
    position: absolute;
    inset: 0;
    background:
      radial-gradient(ellipse at 30% 40%, var(--teal-light) 0%, transparent 60%),
      linear-gradient(160deg, var(--teal-mid) 0%, var(--teal-dark) 100%);
  }
  .hero-copy {
    position: absolute;
    left: 37px;
    top: 122px;
    width: 560px;
  }
  .hero-headline {
    margin: 0;
    font-weight: 700;
    font-size: 50px;
    line-height: 56px;
    letter-spacing: -0.5px;
  }
  .hero-tagline {
    margin: 10px 0 0;
    font-weight: 300;
    font-size: 32px;
    line-height: 34px;
    letter-spacing: -0.3px;
  }
  .equipment-showcase {
    position: absolute;
    left: 572px;
    top: 68px;
    width: 534px;
    height: 366px;
    border-radius: 6px;
    background:
      linear-gradient(100deg, var(--product-dark) 0%, var(--product-dark) 30%, var(--product-mid) 45%, var(--product-light) 70%, var(--product-mid) 100%);
    opacity: 0.92;
  }
</style>
</head>
<body>
  <section class="hero-banner">
    <div class="hero-backdrop" role="img" aria-label="Teal-tinted photo of a conference hall with rows of seats"></div>
    <div class="hero-copy">
      <h1 class="hero-headline">Knowledge. Experience.<br>Results.</h1>
      <p class="hero-tagline">Latest technology solutions offered<br>with the highest industry standards.</p>
    </div>
    <div class="equipment-showcase" role="img" aria-label="Rental equipment photo: wireless handheld microphone, bodypack transmitter, rack receiver and a white office laser printer"></div>
  </section>
</body>
</html>
```